3D Printing Website redesign

We are in the process of redesigning our website. Attached is an image of one of the proposed pages - "The Brightlander". The idea with this page is that site visitors can get an indicative estimate of the cost of 3D Printing based on some provided metrics. When the user alters the metrics the price changes accordingly. We are looking for a design to support this page that will also be used across our site.

```html
<!DOCTYPE html>
<html lang="en">
<head>
<meta charset="utf-8">
<title>Layerline Studio – Pricing &amp; Quotes</title>
<link rel="stylesheet" href="https://fonts.googleapis.com/css2?family=Open+Sans:ital,wght@0,400;0,600;0,700;1,300;1,400;1,700&display=swap">
<style>
  :root {
    --brand-blue: #1c65a8;
    --nav-bg: #525a66;
    --nav-active: #cdd6e1;
    --ink: #3c4048;
    --ink-soft: #4f5560;
    --hero-top: #c2c7cf;
    --hero-bottom: #e7effb;
    --quote-box: #b5b9c0;
    --quote-edge: #a9adb5;
    --panel: #c6cad2;
    --track-border: #474c55;
    --thumb: #b5306c;
    --thumb-edge: #8e2354;
    --white: #ffffff;
    --page: #ffffff;
  }
  * { box-sizing: border-box; margin: 0; padding: 0; }
  html, body { width: 1200px; height: 731px; overflow: hidden; background: var(--page); }
  body { font-family: "Open Sans", Arial, sans-serif; position: relative; }

  .top-bar { position: absolute; left: 0; top: 0; width: 1200px; height: 44px; background: var(--brand-blue); color: var(--white); }
  .top-bar__address { position: absolute; left: 108px; top: 13px; font-size: 14px; font-style: italic; }
  .top-bar__account { position: absolute; right: 109px; top: 12px; font-size: 15px; }
  .top-bar__account b { font-weight: 700; }
  .top-bar__account i { margin: 0 4px; }

  .brand { position: absolute; left: 109px; top: 55px; height: 103px; display: flex; align-items: center; gap: 14px; }
  .brand__mark { width: 100px; height: 100px; border-radius: 50%; background: var(--brand-blue); }
  .brand__name { font-size: 40px; font-weight: 700; color: var(--brand-blue); letter-spacing: 0.5px; }

  .main-nav { position: absolute; left: 109px; top: 164px; width: 982px; height: 52px; background: var(--nav-bg); border-radius: 5px 5px 0 0; display: flex; padding-left: 26px; }
  .main-nav a { color: var(--white); text-decoration: none; font-size: 16px; line-height: 52px; padding: 0 22px; }
  .main-nav a.is-active { background: var(--nav-active); color: var(--ink); padding: 0 17px; }

  .hero { position: absolute; left: 109px; top: 216px; width: 982px; height: 214px; background: linear-gradient(var(--hero-top), var(--hero-bottom) 55%); }
  .hero__quote { position: absolute; left: 196px; top: 20px; width: 590px; height: 96px; background: var(--quote-box); border-radius: 5px; border-bottom: 13px solid var(--quote-edge); color: #f4f4f4; font-size: 64px; font-weight: 300; font-style: italic; text-align: center; line-height: 86px; }
  .hero__or { position: absolute; left: 0; top: 122px; width: 100%; text-align: center; font-size: 64px; font-weight: 700; font-style: italic; color: var(--ink-soft); line-height: 90px; }

  .estimator { position: absolute; left: 109px; top: 430px; width: 982px; height: 301px; background: var(--panel); border-radius: 5px 5px 0 0; }
  .service-btn { position: absolute; left: 30px; width: 218px; height: 109px; background: var(--brand-blue); border-radius: 3px; color: var(--white); font-size: 43px; font-weight: 700; font-style: italic; display: flex; align-items: center; justify-content: center; }

  .metric__label { position: absolute; left: 313px; width: 356px; text-align: center; font-size: 28px; font-weight: 700; color: var(--ink); line-height: 34px; }
  .metric__end { position: absolute; font-size: 18px; font-style: italic; color: var(--ink); }
  .metric__track { position: absolute; left: 313px; width: 356px; height: 26px; background: var(--white); border: 2px solid var(--track-border); border-radius: 6px; }
  .metric__thumb { position: absolute; top: -7px; width: 24px; height: 36px; background: var(--thumb); border: 1px solid var(--thumb-edge); border-radius: 2px; }

  .shape-preview { position: absolute; left: 695px; top: 84px; width: 264px; height: 264px; border-radius: 50%; background: radial-gradient(circle at 50% 32%, #575d68 0%, #4b515b 40%, #3b4049 100%); }
</style>
</head>
<body>
  <header class="top-bar">
    <span class="top-bar__address">This is where you put your address</span>
    <span class="top-bar__account"><b>Log In</b><i>or</i><b>Register</b></span>
  </header>

  <div class="brand">
    <span class="brand__mark"></span>
    <span class="brand__name">Layerline Studio</span>
  </div>

  <nav class="main-nav">
    <a href="#">Shop</a>
    <a href="#">What We Do</a>
    <a href="#" class="is-active">Pricing &amp; Quotes</a>
    <a href="#">Materials</a>
    <a href="#">Gallery</a>
    <a href="#">DIY</a>
    <a href="#">Training</a>
    <a href="#">Contact</a>
    <a href="#">Blog</a>
  </nav>

  <section class="hero">
    <div class="hero__quote">Get an instant quote!</div>
    <div class="hero__or">or</div>
  </section>

  <section class="estimator">
    <div class="service-btn" style="top:30px">PRINT</div>
    <div class="service-btn" style="top:161px">SCAN</div>
    <div class="service-btn" style="top:292px"></div>

    <div class="metric__label" style="top:28px">SHAPE</div>
    <span class="metric__end" style="left:321px;top:52px">Square</span>
    <span class="metric__end" style="left:601px;top:52px">Circular</span>
    <div class="metric__track" style="top:81px"><span class="metric__thumb" style="left:76px"></span></div>

    <div class="metric__label" style="top:129px">SIZE</div>
    <div class="metric__track" style="top:182px"><span class="metric__thumb" style="left:164px"></span></div>

    <div class="metric__label" style="top:229px">VOLUME</div>
    <div class="metric__track" style="top:282px"><span class="metric__thumb" style="left:164px"></span></div>

    <div class="shape-preview" role="img" aria-label="Preview of the selected print shape"></div>
  </section>
</body>
</html>
```